Gruppo Abitativo Sorena
complete stationary set
Gruppo Abitativo Sorena - Real Estate
Creative Brief
Professional
Marcello Ruffoni
Responsabile di agenzia
Gruppo Abitativo Sorena Via Castellana, 147 20384 Milano - Italy
marcello.ruffoni@gruppoabitativosorena.example
www.gruppoabitativosorena.example
I'm looking for a complete set of stationary: 1. Business Cards 2. Letter Head 3. Presentation Folder 6. Envelopes 7. PowerPoint slide template 9. Note pad cover 10. e-mail signature 11. Fax Cover Please insert QR Code and a photo box in business card. For further information post comments or contact me I will give you all feedback you need
Should have something to that represents our company and will make them want to look at the card again.

```html
<!DOCTYPE html>
<html lang="it">
<head>
<meta charset="UTF-8">
<title>Gruppo Abitativo Sorena – Biglietto da visita</title>
<link rel="stylesheet" href="https://fonts.googleapis.com/css2?family=Open+Sans:wght@400;600;700&display=swap">
<style>
  :root {
    --page-bg: #e9e6e1;
    --card-white: #ffffff;
    --navy-deep: #0a1a5c;
    --navy-mid: #152c8a;
    --navy-light: #2a4ab8;
    --brand-blue: #1f3c8f;
    --text-grey: #8a8a8a;
    --text-dark: #3b3b3b;
    --photo-grey: #e6e6e6;
    --photo-label: #d2d2d2;
    --on-navy: #e8ecff;
  }
  * { box-sizing: border-box; margin: 0; padding: 0; }
  html, body {
    width: 1200px; height: 780px; overflow: hidden;
    background: var(--page-bg);
    font-family: "Open Sans", Arial, sans-serif;
  }
  .business-card {
    position: absolute; left: 100px; top: 105px;
    width: 1000px; height: 570px;
    border-radius: 34px; overflow: hidden;
    display: flex;
    box-shadow: 0 18px 40px rgba(0,0,0,.22);
  }
  .card-front {
    width: 480px; background: var(--card-white);
    display: flex; flex-direction: column; align-items: center;
    padding-top: 62px;
  }
  .brand { display: flex; align-items: center; gap: 12px; }
  .brand-mark { width: 26px; height: 26px; background: var(--brand-blue); }
  .brand-name {
    font-weight: 700; font-size: 27px; color: var(--brand-blue);
    text-transform: uppercase; letter-spacing: .2px;
  }
  .brand-web {
    margin-top: 6px; font-size: 12px; color: var(--text-grey); letter-spacing: 1.5px;
  }
  .agent-photo {
    margin-top: 38px; width: 196px; height: 196px;
    background: var(--photo-grey); border-radius: 6px;
    display: flex; align-items: center; justify-content: center;
  }
  .agent-photo-label {
    font-size: 48px; font-weight: 400; color: var(--photo-label);
  }
  .agent-name {
    margin-top: 28px; font-weight: 700; font-size: 31px; color: var(--brand-blue);
  }
  .agent-role {
    margin-top: 2px; font-weight: 600; font-size: 19px; color: var(--text-grey);
  }
  .agent-email {
    margin-top: 22px; font-size: 15px; color: var(--text-dark);
  }
  .card-back {
    flex: 1; position: relative; color: var(--on-navy);
    background: radial-gradient(ellipse 70% 75% at 62% 45%, var(--navy-light), var(--navy-mid) 50%, var(--navy-deep) 100%);
    text-align: right;
  }
  .office-address {
    position: absolute; right: 64px; top: 150px;
    font-size: 20px; line-height: 1.3; font-style: normal;
  }
  .phone-list {
    position: absolute; right: 46px; top: 318px;
    list-style: none; font-size: 20px; line-height: 1.55;
  }
  .phone-list li { display: flex; align-items: center; justify-content: flex-end; gap: 14px; }
  .phone-list svg { width: 22px; height: 22px; fill: var(--on-navy); flex: none; }
</style>
</head>
<body>
  <section class="business-card">
    <div class="card-front">
      <div class="brand">
        <span class="brand-mark"></span>
        <span class="brand-name">Gruppo Abitativo Sorena</span>
      </div>
      <div class="brand-web">www.gruppoabitativosorena.example</div>
      <div class="agent-photo" role="img" aria-label="Spazio per la foto dell'agente">
        <span class="agent-photo-label">Pic</span>
      </div>
      <h1 class="agent-name">Marcello Ruffoni</h1>
      <p class="agent-role">Responsabile di agenzia</p>
      <p class="agent-email">marcello.ruffoni@gruppoabitativosorena.example</p>
    </div>
    <div class="card-back">
      <address class="office-address">
        Gruppo Abitativo Sorena<br>
        Via Castellana, 147<br>
        20384 Milano - Italy
      </address>
      <ul class="phone-list">
        <li>+39 02 555 01 470
          <svg viewBox="0 0 24 24" aria-label="Telefono"><path d="M6.6 10.8a15 15 0 0 0 6.6 6.6l2.2-2.2a1 1 0 0 1 1-.25 11.4 11.4 0 0 0 3.6.57 1 1 0 0 1 1 1V20a1 1 0 0 1-1 1A17 17 0 0 1 3 4a1 1 0 0 1 1-1h3.5a1 1 0 0 1 1 1c0 1.25.2 2.450.57 3.57a1 1 0 0 1-.25 1z"/></svg>
        </li>
        <li>+39 347 555 12 84
          <svg viewBox="0 0 24 24" aria-label="Cellulare"><path d="M8 1h8a2 2 0 0 1 2 2v18a2 2 0 0 1-2 2H8a2 2 0 0 1-2-2V3a2 2 0 0 1 2-2zm0 3v13h8V4zm4 15a1 1 0 1 0 0 2 1 1 0 0 0 0-2z"/></svg>
        </li>
        <li>+39 02 555 01 471
          <svg viewBox="0 0 24 24" aria-label="Fax"><path d="M7 2h8l3 3v5h1a2 2 0 0 1 2 2v8a2 2 0 0 1-2 2H5a2 2 0 0 1-2-2v-8a2 2 0 0 1 2-2h2zm2 2v6h7V6h-2V4zm-2 10v2h3v-2zm5 0v2h5v-2zm-5 3v2h3v-2zm5 0v2h5v-2z"/></svg>
        </li>
      </ul>
    </div>
  </section>
</body>
</html>
```